Wedding Invitation and envelope package

I need the 1st of many invitation designs. This is a floral collection and I have attached many designs that I like from competitors. I think that the pastel look is the best but I am hoping you can make something special. The font selection is just as important as the imagery. The overall size with bleeds is 5.25 x 7.25" and I have attached a sample to make sure sizing is clear. I also need A7 envelopes to go with the invitation, front and back flap. I want someone to look at the design and say they would pick it over any of the samples. I will need 8 total floral designs done over the next few weeks after this 1st one is done. I will also need a collection of 8 modern designs done. Please ask any questions

Font styles to use
Serif
Sans Serif
Script

Requirements
Must have
• This is a single sided invitation, a back side is not needed.
Should not have
• No full solid dark backgrounds

```html
<!DOCTYPE html>
<html lang="en">
<head>
<meta charset="utf-8">
<title>Floral Wedding Suite – Invitation and A7 Envelope</title>
<link rel="stylesheet" href="https://fonts.googleapis.com/css2?family=Great+Vibes&family=Raleway:wght@400;500;600&display=swap">
<style>
  :root {
    --page-bg: #ffffff;
    --envelope-pink: #fbe3e9;
    --envelope-flap: #f9dce4;
    --envelope-liner: #f8e6ee;
    --pocket-edge: #f3d2dc;
    --card-white: #ffffff;
    --rose-line: #efb8c4;
    --ink: #574749;
    --divider: #c9979f;
    --shadow: rgba(120, 80, 90, 0.18);
  }
  * { margin: 0; padding: 0; box-sizing: border-box; }
  html, body {
    width: 1200px;
    height: 1200px;
    overflow: hidden;
    background: var(--page-bg);
  }
  .canvas {
    position: relative;
    width: 1200px;
    height: 1200px;
    overflow: hidden;
  }

  /* decorative artwork areas */
  .floral-bouquet {
    position: absolute;
    left: 750px;
    top: 0;
    width: 450px;
    height: 410px;
    border-radius: 0 0 0 60% / 0 0 0 55%;
    background:
      radial-gradient(circle at 30% 35%, #f7d3bd 0 16%, transparent 30%),
      radial-gradient(circle at 55% 15%, #e7d6ee 0 12%, transparent 26%),
      radial-gradient(circle at 85% 20%, #bcd8a8 0 14%, transparent 30%),
      radial-gradient(circle at 35% 70%, #ee8a98 0 12%, transparent 26%),
      radial-gradient(circle at 70% 60%, #dfe9b8 0 14%, transparent 30%),
      radial-gradient(ellipse at 55% 40%, #f6e6dc 0 40%, transparent 70%);
  }
  .watercolor-wash {
    position: absolute;
    left: 0;
    top: 935px;
    width: 640px;
    height: 265px;
    border-radius: 0 70% 0 0 / 0 90% 0 0;
    background: linear-gradient(160deg, #fdf0f4 0%, #f7cfe0 45%, #f0b3cf 100%);
    opacity: 0.85;
  }

  /* open envelope with invitation */
  .open-envelope {
    position: absolute;
    left: 90px;
    top: 30px;
    width: 650px;
    height: 745px;
    filter: drop-shadow(0 5px 10px var(--shadow));
  }
  .invite-script { font-family: "Great Vibes", cursive; fill: var(--ink); }
  .invite-line {
    font-family: "Raleway", sans-serif;
    font-weight: 600;
    font-size: 11px;
    letter-spacing: 0.5px;
    fill: var(--ink);
  }

  /* envelope back with return address */
  .envelope-back {
    position: absolute;
    left: 458px;
    top: 656px;
    width: 634px;
    height: 415px;
    background: var(--envelope-pink);
    box-shadow: 0 6px 16px var(--shadow);
  }
  .return-address {
    position: absolute;
    left: 68px;
    top: 168px;
    display: flex;
    align-items: center;
    color: var(--ink);
  }
  .couple {
    display: flex;
    flex-direction: column;
    align-items: center;
    width: 190px;
  }
  .couple__first {
    font-family: "Great Vibes", cursive;
    font-size: 46px;
    line-height: 40px;
  }
  .couple__and {
    font-family: "Raleway", sans-serif;
    font-size: 8px;
    font-weight: 600;
    letter-spacing: 0.5px;
    line-height: 8px;
  }
  .couple__surname {
    font-family: "Raleway", sans-serif;
    font-size: 26px;
    font-weight: 400;
    letter-spacing: 1.5px;
    line-height: 28px;
    margin-top: 2px;
  }
  .divider {
    width: 2px;
    height: 124px;
    margin: 0 26px 0 14px;
    background: var(--divider);
  }
  .address {
    font-family: "Raleway", sans-serif;
    font-style: normal;
    font-size: 17px;
    font-weight: 500;
    line-height: 23px;
    letter-spacing: 0.6px;
    text-transform: uppercase;
    white-space: nowrap;
  }
</style>
</head>
<body>
  <main class="canvas">
    <div class="floral-bouquet" role="img" aria-label="Watercolour bouquet of peach roses, lavender blooms, pink buds and green leaves"></div>
    <div class="watercolor-wash" role="img" aria-label="Soft pink watercolour wash"></div>

    <svg class="open-envelope" viewBox="90 30 650 745" aria-label="Open envelope holding the invitation">
      <!-- top flap -->
      <path d="M97 330 L395 50 Q420 30 445 50 L728 330 Z" fill="var(--envelope-flap)"/>
      <path d="M125 330 L400 72 Q420 58 440 72 L700 330 Z" fill="var(--envelope-liner)"/>
      <!-- envelope body -->
      <rect x="97" y="330" width="631" height="432" fill="var(--envelope-pink)"/>
      <!-- invitation card -->
      <rect x="135" y="350" width="570" height="320" fill="var(--card-white)"/>
      <rect x="135" y="350" width="110" height="80" fill="#f6cfe0" opacity="0.7" role="img" aria-label="Pink watercolour corner"/>
      <line x1="225" y1="430" x2="350" y2="352" stroke="var(--rose-line)" stroke-width="3"/>
      <line x1="215" y1="420" x2="580" y2="440" stroke="var(--rose-line)" stroke-width="3"/>
      <line x1="300" y1="360" x2="640" y2="372" stroke="var(--rose-line)" stroke-width="3"/>
      <ellipse cx="552" cy="400" rx="26" ry="34" fill="#7fa6c4" opacity="0.8" role="img" aria-label="Small watercolour songbird"/>
      <rect x="590" y="390" width="60" height="30" rx="12" fill="#dcebc4" opacity="0.8" role="img" aria-label="Green sprig"/>
      <text class="invite-script" font-size="56" transform="translate(335 435) rotate(90)">ond</text>
      <g text-anchor="end">
        <text class="invite-line" transform="translate(410 475) rotate(90)" text-anchor="start">IN THEM</text>
        <text class="invite-line" transform="translate(432 432) rotate(90)" text-anchor="start">THEIR MARRIAGE</text>
        <text class="invite-line" transform="translate(454 470) rotate(90)" text-anchor="start">HTEEN</text>
        <text class="invite-line" transform="translate(476 472) rotate(90)" text-anchor="start">O TWENTY</text>
        <text class="invite-line" transform="translate(498 468) rotate(90)" text-anchor="start">TERNOON</text>
        <text class="invite-line" transform="translate(520 482) rotate(90)" text-anchor="start">132</text>
        <text class="invite-line" transform="translate(542 482) rotate(90)" text-anchor="start">A PARK</text>
      </g>
      <!-- front pocket -->
      <path d="M97 330 L370 545 L97 762 Z" fill="var(--envelope-pink)"/>
      <path d="M728 330 L460 545 L728 762 Z" fill="var(--envelope-pink)"/>
      <path d="M97 762 L330 540 Q415 490 500 540 L728 762 Z" fill="var(--envelope-pink)" stroke="var(--pocket-edge)" stroke-width="2"/>
    </svg>

    <section class="envelope-back">
      <div class="return-address">
        <div class="couple">
          <span class="couple__first">Eleanor</span>
          <span class="couple__and">AND</span>
          <span class="couple__first">Thomas</span>
          <span class="couple__surname">WHITFIELD</span>
        </div>
        <span class="divider" aria-hidden="true"></span>
        <address class="address">
          512 Linden Hill Road<br>
          Suite 418<br>
          Riverton, New York
        </address>
      </div>
    </section>
  </main>
</body>
</html>
```